Brisworth Electric Van Wrap 2023

We need a van wrap designed for our electrical company. We do residential and commercial work. We want the wrap be very eye catching. I want it to included our phone number and website, It must be easy to determine that we are a electrical company and remediable. this need to bee a full van wrap the van will be. the van is velko tarn cargomax cargo van 2021

Target Market(s)

Home owners that need electrical work done

Industry/Entity Type

Electrical services

Colors
0054AA
0677BA
7BADD7
CADEEF
E8F1F8

Requirements
Must have
• phone number- 850-555-0194 , website - www.brisworthelectric.example, included our logo and be very eye catching
Nice to have
• something that will stand out going do the road and know its a electrical company

```html
<!DOCTYPE html>
<html lang="en">
<head>
<meta charset="utf-8">
<title>Brisworth Electric Van Wrap</title>
<link rel="stylesheet" href="https://fonts.googleapis.com/css2?family=Poppins:wght@500;600;700&display=swap">
<style>
  :root {
    --wrap-blue: #27a6e5;
    --wrap-black: #141414;
    --wrap-white: #f4f4f4;
    --text-blue: #2aa9e8;
    --ink: #111111;
    --page: #ffffff;
    --trim: #2a2a2a;
  }
  html, body {
    margin: 0;
    padding: 0;
    width: 1200px;
    height: 1200px;
    overflow: hidden;
    background: var(--page);
    font-family: "Poppins", sans-serif;
  }
  .sheet {
    position: relative;
    width: 1200px;
    height: 1200px;
  }
  .wrap-side {
    position: absolute;
    left: 100px;
    width: 1000px;
    height: 400px;
  }
  .wrap-side--white-band { top: 130px; }
  .wrap-side--blue-band { top: 660px; }
  .wrap-side svg {
    position: absolute;
    inset: 0;
    width: 1000px;
    height: 400px;
  }
  .logo-name {
    position: absolute;
    left: 330px;
    top: 160px;
    width: 240px;
    margin: 0;
    text-align: center;
    color: var(--wrap-blue);
    font-weight: 600;
    font-size: 30px;
    line-height: 1.15;
    letter-spacing: 1px;
  }
  .logo-name span { display: block; }
  .brand-name {
    position: absolute;
    left: 640px;
    top: 50px;
    margin: 0;
    color: var(--text-blue);
    font-weight: 600;
    font-size: 46px;
    line-height: 1.18;
    letter-spacing: 7px;
  }
  .brand-name span { display: block; }
  .contact {
    position: absolute;
    left: 620px;
    top: 214px;
    width: 330px;
    margin: 0;
    text-align: center;
  }
  .contact-phone {
    display: block;
    font-weight: 600;
    font-size: 31px;
    letter-spacing: 2px;
    line-height: 1.1;
  }
  .contact-web {
    display: block;
    font-weight: 500;
    font-size: 16px;
    line-height: 1.4;
    color: var(--ink);
  }
  .wrap-side--white-band .contact-phone { color: var(--text-blue); }
  .wrap-side--blue-band .contact-phone { color: var(--ink); }
  .social-handle {
    position: absolute;
    left: 205px;
    top: 256px;
    font-weight: 600;
    font-size: 11px;
    color: var(--ink);
  }
</style>
</head>
<body>
<main class="sheet">

  <section class="wrap-side wrap-side--white-band" aria-label="Van wrap side, white contact band version">
    <svg viewBox="0 0 1000 400" aria-hidden="true">
      <defs>
        <clipPath id="van-outline-a">
          <path d="M0,400 L0,230 Q10,150 110,110 L330,12 L975,12 Q1000,12 1000,40 L1000,400 Z"/>
        </clipPath>
      </defs>
      <g clip-path="url(#van-outline-a)">
        <rect class="panel-blue" x="0" y="0" width="1000" height="400" fill="var(--wrap-blue)"/>
        <polygon class="panel-white-stripe" points="470,0 530,0 440,400 380,400" fill="var(--wrap-white)"/>
        <polygon class="panel-black" points="530,0 1000,0 1000,400 440,400" fill="var(--wrap-black)"/>
        <rect class="contact-band" x="480" y="210" width="520" height="78" fill="var(--wrap-white)"/>
        <circle class="logo-disc" cx="450" cy="200" r="152" fill="var(--wrap-white)"/>
        <rect class="rocker-trim" x="0" y="370" width="1000" height="30" fill="var(--trim)"/>
      </g>
    </svg>
    <p class="logo-name"><span>BRISWORTH</span><span>ELECTRIC</span></p>
    <span class="social-handle">@brisworthelectric</span>
    <h1 class="brand-name"><span>ELECTRIC</span><span>BRISWORTH</span></h1>
    <p class="contact">
      <span class="contact-phone">850-555-0194</span>
      <span class="contact-web">www.brisworthelectric.example</span>
    </p>
  </section>

  <section class="wrap-side wrap-side--blue-band" aria-label="Van wrap side, blue contact band version">
    <svg viewBox="0 0 1000 400" aria-hidden="true">
      <defs>
        <clipPath id="van-outline-b">
          <path d="M0,400 L0,230 Q10,150 110,110 L330,12 L975,12 Q1000,12 1000,40 L1000,400 Z"/>
        </clipPath>
      </defs>
      <g clip-path="url(#van-outline-b)">
        <rect class="panel-blue" x="0" y="0" width="1000" height="400" fill="var(--wrap-blue)"/>
        <polygon class="panel-white-stripe" points="470,0 530,0 440,400 380,400" fill="var(--wrap-white)"/>
        <polygon class="panel-black" points="530,0 1000,0 1000,400 440,400" fill="var(--wrap-black)"/>
        <rect class="contact-band" x="480" y="210" width="520" height="78" fill="var(--wrap-blue)"/>
        <circle class="logo-disc" cx="450" cy="200" r="152" fill="var(--wrap-white)"/>
        <rect class="rocker-trim" x="0" y="370" width="1000" height="30" fill="var(--trim)"/>
      </g>
    </svg>
    <p class="logo-name"><span>BRISWORTH</span><span>ELECTRIC</span></p>
    <span class="social-handle">@brisworthelectric</span>
    <h2 class="brand-name"><span>ELECTRIC</span><span>BRISWORTH</span></h2>
    <p class="contact">
      <span class="contact-phone">850-555-0194</span>
      <span class="contact-web">www.brisworthelectric.example</span>
    </p>
  </section>

</main>
</body>
</html>
```